Brivo Drafts (Residential House Plans Company)

Want professional landing page to match our company theme. We provide custom house plans for primarily residential. We are structural engineers (not architects).

Prefer dark (black) theme but open to design options. Would like map of office location.

Address: 412 W Larkspur Road, Oviedo, FL 32768
Phone: 407-555-0192
Email: office@brivodrafts.example

Target Market(s)

Client who need custom house plans

Industry/Entity Type

Architecture, Structural Engineering

Coding

Colors
0054AA
0677BA
7BADD7
CADEEF
E8F1F8

```html
<!DOCTYPE html>
<html lang="en">
<head>
<meta charset="utf-8">
<title>Brivo Drafts — Custom Residential House Plans</title>
<link rel="stylesheet" href="https://fonts.googleapis.com/css2?family=EB+Garamond:wght@400;500;600;700;800&family=Lato:wght@400;700&family=Open+Sans:wght@400;600&display=swap">
<style>
:root{
  --black:#000;
  --white:#fff;
  --ink:#1c1c1c;
  --muted:#444;
  --brand:#1f7cc4;
  --brand-deep:#0054AA;
  --brand-mid:#0677BA;
  --sky:#08a3e6;
  --light:#7BADD7;
  --pale:#CADEEF;
  --mist:#E8F1F8;
  --accent-green:#33c24d;
  --rule:#cfcfcf;
}
*{margin:0;padding:0;box-sizing:border-box}
html,body{width:1200px;height:3658px;overflow:hidden;background:var(--black)}
body{position:relative;font-family:"EB Garamond",Georgia,serif;color:var(--white)}
.abs{position:absolute}
.btn{position:absolute;display:flex;align-items:center;justify-content:center;background:var(--brand);color:var(--white);border-radius:34px;font-family:"EB Garamond",serif;font-weight:600;font-size:25px}

/* header */
.site-header{position:absolute;top:0;left:0;width:1200px;height:90px;z-index:3}
.brand{position:absolute;left:104px;top:22px;display:flex;align-items:center;gap:12px;font-family:"Lato",sans-serif;font-weight:700;font-size:32px;color:var(--white);letter-spacing:.5px}
.brand-mark{width:22px;height:22px;background:var(--brand)}
.main-nav{position:absolute;top:34px;right:99px;display:flex;gap:0;font-family:"Lato",sans-serif;font-size:16px}
.main-nav a{color:var(--white);text-decoration:none;margin-left:66px}

/* hero */
.hero{position:absolute;top:0;left:0;width:1200px;height:750px}
.hero-photo{position:absolute;inset:0;background:linear-gradient(180deg,#8d8d8d 0%,#6c6c6c 25%,#3d3d3d 45%,#151515 62%,#000 78%)}
.hero-eyebrow{position:absolute;top:205px;width:1200px;text-align:center;font-size:54px;font-weight:700;letter-spacing:1px}
.hero-title{position:absolute;top:258px;width:1200px;text-align:center;font-size:124px;font-weight:800;line-height:1;letter-spacing:2px}
.hero-lead{position:absolute;top:395px;left:180px;width:840px;text-align:center;font-size:24px;font-weight:700;line-height:44px}
.scroll-cue{position:absolute;left:570px;top:618px}

/* about */
.about-shape{position:absolute;left:38px;top:785px}
.about-photo{position:absolute;left:94px;top:807px;width:457px;height:440px;background:linear-gradient(135deg,#f2f2f2,#d5d5d5 60%,#bdbdbd)}
.about-title{position:absolute;left:606px;top:815px;font-size:42px;font-weight:700}
.about-text{position:absolute;left:611px;top:897px;width:500px;font-size:19px;line-height:44px}

/* plans */
.section-title{position:absolute;width:1200px;text-align:center;font-size:44px;font-weight:700}
.plan-card{position:absolute;left:98px;top:1503px;width:1003px;height:501px;background:var(--white);border-radius:8px;color:var(--ink)}
.plan-tabs{position:absolute;left:38px;top:22px;display:flex;gap:26px;font-size:24px;font-weight:600}
.plan-tabs .active{border-bottom:2px solid var(--brand);padding-bottom:4px}
.plan-name{position:absolute;left:38px;top:92px;font-size:29px;font-weight:600}
.plan-sub{position:absolute;left:38px;top:152px;font-size:24px;font-weight:600}
.spec{position:absolute;left:38px;width:500px;display:flex;justify-content:space-between;font-size:20px;color:var(--muted);padding-bottom:12px;border-bottom:1px solid var(--rule)}
.spec:last-of-type{border-bottom:none}
.plan-btn{left:40px;top:419px;width:387px;height:52px;background:var(--sky)}
.plan-drawing{position:absolute;left:637px;top:25px;width:280px;height:455px;background:linear-gradient(180deg,#f4f4f4,#e3e3e3)}

/* stats */
.stats{position:absolute;left:0;top:2122px;width:1200px;height:356px;background:var(--brand)}
.stat{position:absolute;top:78px;width:260px;text-align:center}
.stat svg{display:block;margin:0 auto}
.stat-rule{width:92px;height:2px;background:var(--accent-green);margin:8px auto 0}
.stat-num{font-size:50px;font-weight:700;line-height:1;margin-top:20px}
.stat-label{font-size:31px;font-weight:700;margin-top:14px}

/* locations */
.locations-bg{position:absolute;left:0;top:2478px;width:1200px;height:740px;background:linear-gradient(180deg,#5a5a5a 0%,#3a3a3a 30%,#151515 65%,#000 100%)}
.loc-title{position:absolute;left:100px;top:2615px;font-size:44px;font-weight:700}
.loc-text{position:absolute;left:105px;top:2710px;width:450px;font-size:14px;font-weight:700;line-height:30px}
.map{position:absolute;left:601px;top:2616px;width:534px;height:534px;border-radius:50%;background:radial-gradient(circle at 50% 45%,#f4f4f4,#e6e6e6 70%,#dadada)}

/* footer */
.foot-head{position:absolute;font-size:21px;font-weight:700}
.quick-links{position:absolute;left:103px;top:3347px;list-style:none;font-family:"Open Sans",sans-serif;font-size:16px;font-weight:600}
.quick-links li{height:30px;display:flex;align-items:center;gap:14px}
.quick-links li::before{content:"»";color:var(--brand);font-size:16px}
.newsletter{position:absolute;left:315px;top:3362px;width:531px;height:54px;background:var(--white);border-radius:6px;display:flex;align-items:center;color:#333;font-family:"Open Sans",sans-serif;font-size:18px;padding-left:15px}
.newsletter .send{position:absolute;right:0;top:9px;width:70px;height:36px;border-left:1px solid #999;display:flex;align-items:center;justify-content:center}
.contact{position:absolute;left:890px;font-family:"Open Sans",sans-serif;font-size:16px;font-weight:600;line-height:21px;display:flex;gap:10px}
.foot-rule{position:absolute;left:110px;top:3552px;width:980px;height:1px;background:#222}
.copyright{position:absolute;top:3576px;width:1200px;text-align:center;font-size:24px}
</style>
</head>
<body>

<header class="site-header">
  <div class="brand"><span class="brand-mark"></span>Brivo Drafts</div>
  <nav class="main-nav">
    <a href="#">Home</a><a href="#">About Us</a><a href="#">Our Services</a><a href="#">Our&nbsp; Plans</a><a href="#">Contact Us</a>
  </nav>
</header>

<section class="hero">
  <div class="hero-photo" role="img" aria-label="Photo of a two-storey house under construction over faded architectural blueprints"></div>
  <div class="hero-eyebrow">WELCOME TO</div>
  <h1 class="hero-title">BRIVO DRAFTS</h1>
  <p class="hero-lead">Lorem ipsum dolor sit amet, consectetur adipiscing elit, sed do eiusmod tempor incididunt ut labore et dolore magna aliqua.</p>
  <a class="btn" style="left:492px;top:500px;width:216px;height:65px">View Detalis</a>
  <svg class="scroll-cue" width="60" height="72" viewBox="0 0 60 72" fill="none" stroke="#fff" stroke-width="3">
    <circle cx="30" cy="40" r="27"/>
    <line x1="30" y1="0" x2="30" y2="46"/>
    <path d="M20 38 L30 50 L40 38 Z" fill="#fff"/>
  </svg>
</section>

<section class="about">
  <svg class="about-shape" width="520" height="500" viewBox="0 0 520 500">
    <polygon points="0,0 455,0 0,362" fill="var(--brand)"/>
    <rect x="27.5" y="50.5" width="445" height="441" fill="none" stroke="var(--sky)" stroke-width="4"/>
  </svg>
  <div class="about-photo" role="img" aria-label="Photo of rolled house floor plan blueprints"></div>
  <h2 class="about-title">ABOUT US</h2>
  <p class="about-text">Sed ut perspiciatis unde omnis iste natus error sit voluptatem accusantium doloremque laudantium, totam rem aperiam, eaque ipsa quae ab illo inventore veritatis et quasi architecto beatae vitae dicta sunt explicabo. Nemo enim ipsam voluptatem quia voluptas sit aspernatur aut odit aut fugit, sed quia consequuntur magni dolores eos qui</p>
  <a class="btn" style="left:613px;top:1194px;width:215px;height:64px">Read More</a>
</section>

<section class="plans">
  <h2 class="section-title" style="top:1408px">OUR PLANS</h2>
  <div class="plan-card">
    <div class="plan-tabs"><span>Exterior</span><span>Interior</span><span class="active">Floor Plan</span></div>
    <h3 class="plan-name">NEMO ENIM IPSAM</h3>
    <h4 class="plan-sub">Floor Plan</h4>
    <div class="spec" style="top:200px"><span>Total Built-Up Area</span><span>77.5 m2</span></div>
    <div class="spec" style="top:251px"><span>Plot Size</span><span>67 Ft. x 45 Ft.</span></div>
    <div class="spec" style="top:302px"><span>Floors</span><span>2 Nos</span></div>
    <div class="spec" style="top:360px;border-bottom:none"><span>Overall Size of Building</span><span>67 ft x 45 Ft.</span></div>
    <a class="btn plan-btn">Talk to Our Agent(s)</a>
    <div class="plan-drawing" role="img" aria-label="Technical floor plan drawings of the first and second floors"></div>
  </div>
</section>

<section class="stats">
  <div class="stat" style="left:50px">
    <svg width="80" height="80" viewBox="0 0 80 80" fill="none" stroke="#fff" stroke-width="3"><rect x="28" y="6" width="30" height="48"/><rect x="14" y="24" width="16" height="30"/><path d="M34 14h4M44 14h4M34 24h4M44 24h4M34 34h4M44 34h4M20 32h4M20 42h4"/><path d="M4 58c10 0 16 8 30 8h30l10-8"/></svg>
    <div class="stat-rule"></div><div class="stat-num">570</div><div class="stat-label">PROJECTS</div>
  </div>
  <div class="stat" style="left:329px">
    <svg width="80" height="80" viewBox="0 0 80 80" fill="none" stroke="#fff" stroke-width="3"><path d="M40 76C24 54 14 42 14 28a26 26 0 0 1 52 0c0 14-10 26-26 48z"/><circle cx="40" cy="28" r="11"/></svg>
    <div class="stat-rule"></div><div class="stat-num">48</div><div class="stat-label">CITIES</div>
  </div>
  <div class="stat" style="left:606px">
    <svg width="80" height="80" viewBox="0 0 80 80" fill="none" stroke="#fff" stroke-width="3"><rect x="30" y="6" width="20" height="64"/><rect x="12" y="30" width="18" height="40"/><rect x="50" y="22" width="18" height="48"/><path d="M36 16h8M36 28h8M36 40h8M36 52h8M17 40h8M17 52h8M55 32h8M55 44h8M55 56h8M6 70h68"/></svg>
    <div class="stat-rule"></div><div class="stat-num">2410</div><div class="stat-label">HOUSES BUILT</div>
  </div>
  <div class="stat" style="left:888px">
    <svg width="80" height="80" viewBox="0 0 80 80" fill="none" stroke="#fff" stroke-width="3"><rect x="28" y="6" width="30" height="48"/><rect x="14" y="24" width="16" height="30"/><path d="M34 14h4M44 14h4M34 24h4M44 24h4M34 34h4M44 34h4M20 32h4M20 42h4"/><path d="M4 58c10 0 16 8 30 8h30l10-8"/></svg>
    <div class="stat-rule"></div><div class="stat-num">1000</div><div class="stat-label">WORKERS</div>
  </div>
</section>

<section class="locations">
  <div class="locations-bg" role="img" aria-label="Faded photo of a finished two-storey house fading into black"></div>
  <h2 class="loc-title">OUR LOCATIONS</h2>
  <p class="loc-text">Lorem ipsum dolor sit amet, consectetur adipiscing elit, sed do eiusmod tempor incididunt ut labore et dolore magna aliqua. Ut enim ad minim veniam, quis nostrud exercitation ullamco laboris nisi ut aliquip ex ea commodo consequat. Duis aute irure dolor in reprehenderit in voluptate velit esse cillum dolore eu fugiat nulla pariatur. Lorem ipsum dolor sit amet, consectetur adipiscing elit, sed do eiusmod tempor incididunt ut labore et dolore magna aliqua. Ut enim ad minim veniam, quis nostrud exercitation ullamco laboris nisi ut aliquip ex ea commodo consequat. Duis aute irure dolor in reprehenderit in voluptate velit esse cillum dolore eu fugiat nulla pariatur.</p>
  <a class="btn" style="left:110px;top:3078px;width:216px;height:65px">View Detalis</a>
  <div class="map" role="img" aria-label="Street map of the Oviedo office location with a marker on the office"></div>
</section>

<footer>
  <h4 class="foot-head" style="left:103px;top:3295px">QUICK LINKS</h4>
  <ul class="quick-links">
    <li>Home</li><li>About Us</li><li>Our Services</li><li>Our&nbsp; Plans</li><li>Contact Us</li>
  </ul>

  <h4 class="foot-head" style="left:362px;top:3296px;font-size:26px">SUBSCRIBE TO FREE&nbsp; NEWSLETTERS</h4>
  <div class="newsletter">Enter your email
    <span class="send"><svg width="26" height="24" viewBox="0 0 26 24"><path d="M1 11 L25 1 L17 23 L12 14 Z" fill="#222"/><path d="M12 14 L25 1" stroke="#fff" stroke-width="1.5"/></svg></span>
  </div>

  <h4 class="foot-head" style="left:890px;top:3295px">GET IN TOUCH</h4>
  <div class="contact" style="top:3346px">
    <svg width="12" height="16" viewBox="0 0 12 16"><path d="M6 16C2 10 0 8 0 6a6 6 0 0 1 12 0c0 2-2 4-6 10z" fill="#fff"/><circle cx="6" cy="6" r="2" fill="#000"/></svg>
    <span>412 W Larkspur Road<br>Oviedo, FL 32768</span>
  </div>
  <div class="contact" style="top:3430px">
    <svg width="14" height="14" viewBox="0 0 14 14"><path d="M3 0l3 3-2 2c1 2 3 4 5 5l2-2 3 3-2 3C6 14 0 8 0 3z" fill="#fff"/></svg>
    <span>+1 407-555-0192</span>
  </div>
  <div class="contact" style="top:3479px">
    <svg width="15" height="12" viewBox="0 0 15 12" fill="none" stroke="#fff" stroke-width="1.6"><rect x="1" y="1" width="13" height="10"/><path d="M1 1l6.5 6L14 1"/></svg>
    <span>office@brivodrafts.example</span>
  </div>

  <div class="foot-rule"></div>
  <p class="copyright">© copyrights 2023 Brivo Drafts |&nbsp; All Rights Reserved</p>
</footer>

</body>
</html>
```